Brava Nest (Smart Home, Installation, Repair Industry) (Contest)

Looking for a website design for my company
Services we offer:
Phone Repair
TV Mounting
Security Camera Installation
Networking / Wi-Fi
Smart Home Services
IT Support

Looking for a website similar to trovely.example

Few tabs
About Us
Contact Us
Areas Served
Pricing and Services

```html
<!DOCTYPE html>
<html lang="en">
<head>
<meta charset="utf-8">
<title>Brava Nest – Repair Your Appliances</title>
<link href="https://fonts.googleapis.com/css2?family=Ubuntu:wght@400;500;700&display=swap" rel="stylesheet">
<style>
:root{
  --navy:#0b4a66;
  --navy-deep:#083a52;
  --orange:#f39322;
  --orange-soft:rgba(243,147,34,.85);
  --icon-blue:#1d6fd8;
  --text:#1f2d3a;
  --white:#ffffff;
}
*{margin:0;padding:0;box-sizing:border-box}
html,body{width:1200px;height:3108px;overflow:hidden;background:var(--white)}
body{position:relative;font-family:'Ubuntu',sans-serif;color:var(--text)}
.abs{position:absolute}
a{color:inherit;text-decoration:none}

/* hero */
.hero{left:7px;top:0;width:1193px;height:450px;
  background:linear-gradient(90deg,#6b5646 0%,#7a6252 45%,#5e5048 60%,#0f4a66 68%,#0c4762 100%)}
.hero-sky{left:7px;top:0;width:1193px;height:140px;background:linear-gradient(180deg,#0b4661,rgba(11,70,97,0))}
.logo{left:150px;top:4px;font-size:34px;font-weight:700;color:var(--orange)}
.nav{top:15px;font-size:13px;font-weight:700;color:var(--white);letter-spacing:.2px}
.hero-card{left:150px;top:116px;width:412px;height:224px;background:var(--white);padding:30px 15px}
.hero-card h1{font-size:32px;font-weight:700;color:var(--navy);line-height:1.1}
.hero-card p{margin-top:14px;font-size:18px;line-height:27px;color:#333}
.btn{display:flex;align-items:center;justify-content:center;background:var(--orange);color:var(--white);
  font-size:13px;font-weight:500;border-radius:20px}
.hero-card .btn{position:absolute;left:14px;top:149px;width:187px;height:37px}

/* service icons */
.svc{width:150px;text-align:center;font-size:13px;line-height:20px;color:#333}
.svc svg{display:block;margin:0 auto 14px}

/* about */
.about-photo{left:152px;top:736px;width:479px;height:317px;background:linear-gradient(120deg,#3b4450 0%,#7b7f86 40%,#e4e6e8 65%,#f4f5f6 100%)}
.h2{font-size:24px;font-weight:700;color:var(--navy)}
.rule{height:4px;background:var(--orange);border-radius:2px}
.about-text{left:693px;top:800px;width:345px;font-size:13.3px;line-height:20.2px;color:#1f3a5a}
.about-text p+p{margin-top:20px}

/* contact band */
.band{left:0;top:1131px;width:1200px;height:111px;background:var(--white);box-shadow:0 0 30px rgba(0,0,0,.12)}
.band-label{left:409px;top:1164px;font-size:13px;font-weight:700;color:var(--navy)}
.band-number{left:409px;top:1187px;font-size:24px;color:var(--navy);font-weight:500}

/* areas */
.feature{width:160px;text-align:center;font-size:13px;font-weight:500;color:var(--navy)}
.area-photo{left:371px;top:1403px;width:675px;height:373px;
  background:linear-gradient(180deg,#a9cbe6 0%,#d9e3ea 35%,#c89a7e 55%,#e8e8e6 75%,#5fb8c9 100%)}
.tag{width:145px;height:58px;background:var(--white);display:flex;align-items:center;justify-content:center;
  text-align:center;font-size:13px;font-weight:500;line-height:20px;color:#1d2b38}
.tag svg{position:absolute;left:-4px;top:-10px}

/* services grid */
.card{width:299px;height:374px;overflow:hidden}
.card-bar{position:absolute;left:0;bottom:0;width:100%;height:74px;background:var(--orange-soft);
  display:flex;align-items:center;justify-content:center;text-align:center;color:var(--white);font-size:18px;font-weight:700;line-height:21px}
.card-overlay{position:absolute;left:0;top:149px;width:100%;height:151px;background:rgba(243,147,34,.78);
  padding:16px 3px;font-size:11.5px;line-height:20px;color:var(--white)}
.card-price{justify-content:flex-start;text-align:left;padding-left:15px;font-weight:400;font-size:17px}

/* footer */
.footer{left:0;top:2770px;width:1200px;height:279px;background:var(--navy)}
.foot-col{top:2822px;color:var(--white)}
.foot-col h3{font-size:19px;font-weight:500;margin-bottom:18px}
.foot-col li{list-style:none;font-size:14px;line-height:27px}
.copy{left:0;top:3049px;width:1200px;height:21px;background:#0a1a22;color:var(--white);font-size:12px;
  display:flex;align-items:center;justify-content:center}
</style>
</head>
<body>

<!-- Hero -->
<div class="abs hero" role="img" aria-label="Brick building facade against a deep blue sky"></div>
<div class="abs hero-sky"></div>
<div class="abs logo">Brava Nest</div>
<a class="abs nav" style="left:544px">ABOUT US</a>
<a class="abs nav" style="left:651px">CONTACT US</a>
<a class="abs nav" style="left:773px">AREAS SERVED</a>
<a class="abs nav" style="left:913px">PRICING &amp; SERVICES</a>
<section class="abs hero-card">
  <h1>Repair Your Appliances</h1>
  <p>Repair your home appliances by highky trained professional technicians</p>
  <a class="btn">Book a Service</a>
</section>

<!-- Service icons -->
<div class="abs svc" style="left:130px;top:525px">
  <svg width="78" height="74" viewBox="0 0 78 74" fill="none" stroke="var(--icon-blue)" stroke-width="2.5">
    <rect x="30" y="2" width="42" height="70" rx="5"/><line x1="30" y1="12" x2="72" y2="12"/><line x1="30" y1="60" x2="72" y2="60"/>
    <circle cx="52" cy="36" r="9" stroke="var(--orange)"/><path d="M2 30h24l6 6-6 6H2z"/>
  </svg>Mobile Repair</div>
<div class="abs svc" style="left:307px;top:525px">
  <svg width="80" height="74" viewBox="0 0 80 74" fill="none" stroke="var(--icon-blue)" stroke-width="2.5">
    <path d="M30 8l46 22-8 16-46-22z"/><circle cx="68" cy="36" r="3" stroke="var(--orange)"/>
    <path d="M34 34l-6 14H14"/><line x1="6" y1="34" x2="6" y2="68"/><line x1="6" y1="50" x2="14" y2="50"/>
  </svg>Security Camera<br>Installationa</div>
<div class="abs svc" style="left:524px;top:525px">
  <svg width="78" height="74" viewBox="0 0 78 74" fill="none" stroke="var(--icon-blue)" stroke-width="2.5">
    <rect x="4" y="16" width="26" height="34" rx="5"/><rect x="10" y="2" width="14" height="14"/><rect x="10" y="50" width="14" height="14"/>
    <circle cx="17" cy="33" r="6" stroke="var(--orange)"/><path d="M42 22L60 6l18 16v24H42z"/><rect x="52" y="26" width="16" height="12"/>
    <path d="M30 70h30"/><circle cx="66" cy="66" r="8" stroke="var(--orange)"/>
  </svg>Smart Home<br>Services</div>
<div class="abs svc" style="left:727px;top:525px">
  <svg width="80" height="70" viewBox="0 0 80 70" fill="none" stroke="var(--icon-blue)" stroke-width="2.5">
    <path d="M4 8c24-4 48-4 72 0v46c-24 4-48 4-72 0z"/><path d="M10 14c20-3 40-3 60 0v34c-20 3-40 3-60 0z" stroke="var(--orange)"/>
    <path d="M32 56v10M48 56v10M26 66h28"/>
  </svg>T.V Mounting</div>
<div class="abs svc" style="left:922px;top:525px">
  <svg width="80" height="74" viewBox="0 0 80 74" fill="none" stroke="var(--icon-blue)" stroke-width="2.5">
    <path d="M4 26a52 52 0 0 1 72 0"/><path d="M14 36a38 38 0 0 1 52 0"/><path d="M24 46a24 24 0 0 1 32 0"/><path d="M32 54a12 12 0 0 1 16 0"/>
    <circle cx="40" cy="64" r="4" stroke="var(--orange)"/>
  </svg>Netwroking /<br>Wi-Fi</div>

<!-- About -->
<div class="abs about-photo" role="img" aria-label="Technician in a hard hat fitting a wall socket"></div>
<h2 class="abs h2" style="left:693px;top:735px">About Us</h2>
<div class="abs rule" style="left:693px;top:776px;width:226px"></div>
<div class="abs about-text">
  <p>Lorem ipsum dolor sit amet, consectetur adipiscing elit, sed do eiusmod tempor incididunt ut labore et dolore magna aliqua. Quis ipsum suspendisse ultrices gravida. Risus commodo viverra maecenas accumsan lacus vel facilisis.</p>
  <p>Lorem ipsum dolor sit amet, consectetur adipiscing elit, sed do eiusmod tempor incididunt ut labore et dolore magna aliqua. Quis ipsum suspendisse ultrices gravida. Risus commodo viverra maecenas accumsan lacus vel facilisis.</p>
</div>

<!-- Contact band -->
<div class="abs band"></div>
<svg class="abs" style="left:323px;top:1154px" width="64" height="64" viewBox="0 0 24 24" fill="var(--navy)">
  <path d="M6.6 10.8a15.1 15.1 0 0 0 6.6 6.6l2.2-2.2a1 1 0 0 1 1-.25 11.4 11.4 0 0 0 3.6.57 1 1 0 0 1 1 1V20a1 1 0 0 1-1 1A17 17 0 0 1 3 4a1 1 0 0 1 1-1h3.5a1 1 0 0 1 1 1c0 1.25.2 2.45.57 3.57a1 1 0 0 1-.25 1z"/>
</svg>
<div class="abs band-label">CONACT US</div>
<div class="abs band-number">022.481.903.6</div>
<a class="abs btn" style="left:689px;top:1169px;width:187px;height:36px">Book a Service</a>

<!-- Areas served -->
<h2 class="abs h2" style="left:150px;top:1320px">Areas Served</h2>
<div class="abs rule" style="left:147px;top:1362px;width:226px"></div>

<div class="abs feature" style="left:180px;top:1405px">
  <svg width="70" height="66" viewBox="0 0 70 66" fill="none" stroke="var(--icon-blue)" stroke-width="3">
    <rect x="3" y="28" width="14" height="35"/><path d="M17 30l14-16 4-12c6 0 8 6 6 14l-2 8h22c4 0 6 4 4 8l-2 4 2 4-3 5 2 5-4 6H17"/>
  </svg>
  <div style="margin-top:8px">Trusted Technicians</div></div>
<div class="abs feature" style="left:180px;top:1545px">
  <svg width="56" height="68" viewBox="0 0 56 68" fill="none" stroke="var(--icon-blue)" stroke-width="3">
    <path d="M28 3L53 14v20c0 16-11 26-25 31C14 60 3 50 3 34V14z"/><path d="M18 34l8 8 14-14" stroke="var(--orange)"/>
  </svg>
  <div style="margin-top:8px">Guarented Parts</div></div>
<div class="abs feature" style="left:173px;top:1686px">
  <svg width="70" height="66" viewBox="0 0 70 66" fill="none" stroke="var(--icon-blue)" stroke-width="3">
    <path d="M4 8l8-6 50 50-4 8z"/><circle cx="62" cy="58" r="5"/><path d="M66 8a10 10 0 0 1-14 12L14 58l-6-6 38-38A10 10 0 0 1 58 2l-6 6 4 4z"/>
  </svg>
  <div style="margin-top:8px">24/7&nbsp; Service</div></div>

<div class="abs area-photo" role="img" aria-label="Modern white two-storey house with pool"></div>
<div class="abs tag" style="left:637px;top:1445px"><svg width="48" height="22" viewBox="0 0 48 22"><path d="M4 20L34 6" stroke="var(--orange)" stroke-width="5" stroke-linecap="round"/><circle cx="38" cy="6" r="6" fill="var(--orange)"/><circle cx="40" cy="3" r="3" fill="#fff"/></svg>Netwroking /<br>Wi-Fi</div>
<div class="abs tag" style="left:464px;top:1517px"><svg width="48" height="22" viewBox="0 0 48 22"><path d="M4 20L34 6" stroke="var(--orange)" stroke-width="5" stroke-linecap="round"/><circle cx="38" cy="6" r="6" fill="var(--orange)"/><circle cx="40" cy="3" r="3" fill="#fff"/></svg>IT<br>Support</div>
<div class="abs tag" style="left:838px;top:1492px"><svg width="48" height="22" viewBox="0 0 48 22"><path d="M4 20L34 6" stroke="var(--orange)" stroke-width="5" stroke-linecap="round"/><circle cx="38" cy="6" r="6" fill="var(--orange)"/><circle cx="40" cy="3" r="3" fill="#fff"/></svg>Smart Home<br>Services</div>
<div class="abs tag" style="left:493px;top:1649px"><svg width="48" height="22" viewBox="0 0 48 22"><path d="M4 20L34 6" stroke="var(--orange)" stroke-width="5" stroke-linecap="round"/><circle cx="38" cy="6" r="6" fill="var(--orange)"/><circle cx="40" cy="3" r="3" fill="#fff"/></svg>T.V.<br>Mounting</div>
<div class="abs tag" style="left:866px;top:1645px"><svg width="48" height="22" viewBox="0 0 48 22"><path d="M4 20L34 6" stroke="var(--orange)" stroke-width="5" stroke-linecap="round"/><circle cx="38" cy="6" r="6" fill="var(--orange)"/><circle cx="40" cy="3" r="3" fill="#fff"/></svg>Security Camera<br>Installation</div>

<!-- Services and charges -->
<h2 class="abs h2" style="left:150px;top:1852px">Services and Charges</h2>
<div class="abs rule" style="left:147px;top:1895px;width:226px"></div>

<div class="abs card" style="left:148px;top:1931px;background:linear-gradient(135deg,#e9eaec,#c6ccd6 50%,#5b86c9)" role="img" aria-label="Smartphone on a table">
  <div class="card-overlay">Lorem ipsum dolor sit amet, consectetur adipiscing elit, sed do eiusmod tempor incididunt ut labore et dolore magna aliqua. Quis ipsum suspendisse ultrices gravida. Risus commodo viverra maecenas accumsan lacus vel facilisis.</div>
  <div class="card-bar card-price">Service Charges : $ 10<br>Extra Charges : $ 20</div>
</div>
<div class="abs card" style="left:447px;top:1931px;background:linear-gradient(180deg,#1c2740 0%,#9a8aa8 40%,#cfd6e4 55%,#1c2438 80%)" role="img" aria-label="Wall-mounted television showing mountains">
  <div class="card-bar">T.V Mounting</div></div>
<div class="abs card" style="left:746px;top:1931px;background:linear-gradient(180deg,#c9c9c9,#e4e4e4 50%,#bdbdbd)" role="img" aria-label="Security camera on a perforated wall">
  <div class="card-bar">Security Camera<br>Installation</div></div>

<div class="abs card" style="left:148px;top:2321px;background:linear-gradient(180deg,#2a2a2a,#4a4a4a 55%,#1b1b1b)" role="img" aria-label="Network router ports">
  <div class="card-bar" style="height:72px">Network and Wi-Fi</div></div>
<div class="abs card" style="left:447px;top:2321px;background:linear-gradient(90deg,#e6e7e8,#bfc1c3 50%,#2d2d2d)" role="img" aria-label="Smart home devices">
  <div class="card-bar" style="height:72px">Smart Home Services</div></div>
<div class="abs card" style="left:746px;top:2321px;background:linear-gradient(160deg,#1a2a55,#24386b 50%,#0f1a36)" role="img" aria-label="Code on a screen">
  <div class="card-bar" style="height:72px">IT Services</div></div>

<!-- Footer -->
<footer class="abs footer"></footer>
<div class="abs foot-col" style="left:193px"><h3>IMPORTANT LINKS</h3><ul><li>ABOUT US</li><li>CONTACT US</li><li>AREAS SERVED</li><li>SERVICES AND PRICES</li></ul></div>
<div class="abs foot-col" style="left:495px"><h3>IMPORTANT LINKS</h3><ul><li>ABOUT US</li><li>CONTACT US</li><li>AREAS SERVED</li><li>SERVICES AND PRICES</li></ul></div>
<div class="abs foot-col" style="left:797px;top:2820px"><h3>IMPORTANT LINKS</h3><ul><li>ABOUT US</li><li>CONTACT US</li><li>AREAS SERVED</li><li>SERVICES AND PRICES</li></ul></div>
<div class="abs copy">Copyright 2020 @ Brava Nest</div>

</body>
</html>
```